Needing a business Card for new fire company.

Velm, sales fire equipment and parts. We also do tree clearing for the forest service. My logo will be attached to this. I am also looking for a design that when people see the card it stick with them and they will remember my sales team giving it to them.

```html
<!DOCTYPE html>
<html lang="en">
<head>
<meta charset="utf-8">
<title>Velm business card</title>
<link href="https://fonts.googleapis.com/css2?family=Marcellus&display=swap" rel="stylesheet">
<style>
  :root{
    --backdrop:#2b2b2b;
    --card:#f4f4f4;
    --card-shade:#e6e6e6;
    --ink:#141414;
    --text:#3a3a3a;
    --fire:#b0202a;
  }
  *{margin:0;padding:0;box-sizing:border-box}
  html,body{width:1200px;height:900px;overflow:hidden}
  body{background:var(--backdrop);font-family:"Marcellus",serif;position:relative}
  .card{
    position:absolute;left:250px;width:700px;height:400px;border-radius:28px;
    background:linear-gradient(120deg,var(--card-shade),var(--card) 45%,#ffffff);
  }
  .card--front{top:40px}
  .card--back{top:460px}
  .wordmark{
    display:flex;align-items:center;gap:18px;
    font-size:96px;letter-spacing:10px;color:var(--ink);line-height:1;
  }
  .wordmark__dot{width:26px;height:26px;border-radius:50%;background:var(--fire)}
  .card--front .wordmark{position:absolute;left:50%;top:50%;transform:translate(-50%,-50%)}
  .card--back .wordmark{position:absolute;left:60px;top:95px;font-size:80px;letter-spacing:8px}
  .person{position:absolute;right:270px;top:210px;text-align:right}
  .person__role{font-size:19px;color:var(--text)}
  .person__name{font-size:24px;color:var(--fire);letter-spacing:1px;margin-top:2px}
  .divider{position:absolute;left:450px;top:170px;width:2px;height:190px;background:var(--ink)}
  .contacts{position:absolute;left:470px;top:170px;list-style:none;font-size:17px;color:var(--text)}
  .contacts li{display:flex;align-items:flex-start;gap:10px;line-height:1.35;margin-bottom:6px}
  .contacts li.address{margin-top:14px}
  .contacts svg{width:16px;height:16px;flex:none;margin-top:3px;fill:var(--fire)}
</style>
</head>
<body>
  <section class="card card--front">
    <div class="wordmark"><span class="wordmark__dot"></span>VELM</div>
  </section>

  <section class="card card--back">
    <div class="wordmark"><span class="wordmark__dot"></span>VELM</div>
    <div class="person">
      <p class="person__role">Director</p>
      <p class="person__name">DARA OLSEN</p>
    </div>
    <div class="divider"></div>
    <ul class="contacts">
      <li><svg viewBox="0 0 24 24"><path d="M6.6 10.8a15.1 15.1 0 0 0 6.6 6.6l2.2-2.2c.3-.3.7-.4 1-.2 1.1.4 2.3.6 3.6.6.6 0 1 .4 1 1V20c0 .6-.4 1-1 1A17 17 0 0 1 3 4c0-.6.4-1 1-1h3.5c.6 0 1 .4 1 1 0 1.3.2 2.5.6 3.6.1.3 0 .7-.2 1z"/></svg>(00) 0000 0000</li>
      <li><svg viewBox="0 0 24 24"><path d="M12 2a10 10 0 1 0 0 20 10 10 0 0 0 0-20zm0 2c1 0 2.4 2 3 5H9c.6-3 2-5 3-5zM4.3 11h3.6a18 18 0 0 0 0 2H4.3a8 8 0 0 1 0-2zm5.7 0h4a16 16 0 0 1 0 2h-4a16 16 0 0 1 0-2zm6.1 0h3.6a8 8 0 0 1 0 2h-3.6a18 18 0 0 0 0-2zM9 15h6c-.6 3-2 5-3 5s-2.4-2-3-5z"/></svg>www.velm.com</li>
      <li><svg viewBox="0 0 24 24"><path d="M3 5h18v14H3zm2 2v.5l7 5 7-5V7zm0 3v7h14v-7l-7 5z"/></svg>dara@velm.com</li>
      <li class="address"><svg viewBox="0 0 24 24"><path d="M12 2a7 7 0 0 0-7 7c0 5 7 13 7 13s7-8 7-13a7 7 0 0 0-7-7zm0 9.5a2.5 2.5 0 1 1 0-5 2.5 2.5 0 0 1 0 5z"/></svg>11 dummy city, dummy place<br>P.O Box 0000 Dummy Land</li>
    </ul>
  </section>
</body>
</html>
```